Modern business card for triathlon training business in Australia

We need a business card design for our triathlon training company.

Pace with Us Fitness is an Australian business, owned by women, run for women. Pace with Us Fitness helps women prepare or improve triathlon skills and confidence through triathlon camps completely designed for women.

Our camps focus on preparing women both physically and mentally for their next (or first!) triathlon.

You can see our website www.pacewithusfitness.com.au for more info about our business and our style.

We've attached two of our logos and are happy to consider a design that utilised either colour scheme with the teal colour being our 'feature' colour. We don't want overly feminine cards but rather cards that are professional and neat. If the inclusion of any pictures/art is warranted, this should be focused on our swim/ride/run theme and in that specific order (swim/ride/run).

The business card needs to be a printable design and the contact details will need to change for our two employees.

Target Market(s)

Female clients and partners/vendors/sponsors that we work with in the triathlon industry

Industry/Entity Type

Fitness

Contact Information for Business Card

Pace with Us Fitness (business name)
Nina Carver
Business Director
Mobile: 0438 916 207
Email: nina@pacewithusfitness.com.au
www.pacewithusfitness.com.au

Second business card:
Pace with Us Fitness
Bel Stray
Coaching Director
Mobile: 0459 260 718
Email: bel@pacewithusfitness.com.au

Font styles to use
Serif
Sans Serif

Requirements
Must have
• Core contact details above, our logo and be a printable design
Should not have
• Pink
• Cursive/script fonts

```html
<!DOCTYPE html>
<html lang="en">
<head>
<meta charset="utf-8">
<title>Pace with Us Fitness – Business Card</title>
<link rel="stylesheet" href="https://fonts.googleapis.com/css2?family=Lato:wght@400;700;900&display=swap">
<style>
  :root {
    --backdrop: #e6e7e8;
    --card: #ffffff;
    --teal: #2bb6c9;
    --ink: #1a1a1a;
    --body: #2b2b2b;
    --grey: #6d6e71;
    --rule: #b9babc;
  }
  * { margin: 0; padding: 0; box-sizing: border-box; }
  html, body {
    width: 1200px;
    height: 898px;
    overflow: hidden;
    background: var(--backdrop);
    font-family: "Lato", Arial, sans-serif;
  }
  .card {
    position: absolute;
    left: 160px;
    top: 180px;
    width: 880px;
    height: 538px;
    background: var(--card);
    box-shadow: 0 6px 24px rgba(0, 0, 0, 0.12);
    overflow: hidden;
  }
  .tab {
    position: absolute;
    height: 16px;
    background: var(--teal);
  }
  .tab--top {
    left: 240px;
    width: 250px;
    top: 0;
    border-radius: 0 0 8px 8px;
  }
  .tab--bottom {
    left: 370px;
    width: 300px;
    bottom: 0;
    border-radius: 8px 8px 0 0;
  }
  .divider {
    position: absolute;
    left: 400px;
    top: 140px;
    width: 1px;
    height: 250px;
    background: var(--rule);
  }
  .contact {
    position: absolute;
    left: 72px;
    top: 176px;
  }
  .contact__name {
    font-weight: 900;
    font-size: 26px;
    letter-spacing: 0.5px;
    color: var(--ink);
    text-transform: uppercase;
    line-height: 1.1;
  }
  .contact__role {
    font-weight: 400;
    font-size: 21px;
    letter-spacing: 0.5px;
    color: var(--teal);
    text-transform: uppercase;
    margin-top: 2px;
  }
  .contact__list {
    list-style: none;
    margin-top: 28px;
  }
  .contact__item {
    display: flex;
    align-items: center;
    gap: 20px;
    font-size: 21px;
    color: var(--body);
    line-height: 1.55;
  }
  .contact__icon {
    width: 16px;
    height: 16px;
    flex: none;
  }
  .brand {
    position: absolute;
    left: 470px;
    top: 210px;
    display: flex;
    align-items: center;
    gap: 18px;
  }
  .brand__dot {
    width: 44px;
    height: 44px;
    border-radius: 50%;
    background: var(--teal);
    flex: none;
  }
  .brand__name {
    font-weight: 900;
    font-size: 30px;
    letter-spacing: 0.5px;
    color: var(--teal);
    text-transform: uppercase;
  }
</style>
</head>
<body>
  <main class="card">
    <div class="tab tab--top"></div>
    <div class="tab tab--bottom"></div>

    <section class="contact">
      <h1 class="contact__name">Bel Stray</h1>
      <p class="contact__role">Coaching Director</p>
      <ul class="contact__list">
        <li class="contact__item">
          <svg class="contact__icon" viewBox="0 0 16 16" aria-hidden="true">
            <path d="M3.5 1.5l2.5 0 1 3.5-1.8 1.2a8 8 0 0 0 4.6 4.6L11 9l3.5 1v2.5c0 1-1 2-2 2C6.5 14.5 1.5 9.5 1.5 3.5c0-1 1-2 2-2z" fill="var(--teal)"/>
          </svg>
          <span>0459 260 718</span>
        </li>
        <li class="contact__item">
          <svg class="contact__icon" viewBox="0 0 16 16" aria-hidden="true">
            <rect x="1" y="3" width="14" height="10" rx="1" fill="var(--teal)"/>
            <path d="M1.5 3.8L8 9l6.5-5.2" fill="none" stroke="#fff" stroke-width="1.3"/>
          </svg>
          <span>bel@pacewithusfitness.com.au</span>
        </li>
        <li class="contact__item">
          <svg class="contact__icon" viewBox="0 0 16 16" aria-hidden="true">
            <rect x="1" y="2" width="14" height="12" rx="1" fill="none" stroke="var(--teal)" stroke-width="1.5"/>
            <rect x="1" y="2" width="14" height="3.5" fill="var(--teal)"/>
            <rect x="3.5" y="8" width="9" height="1.5" fill="var(--teal)"/>
            <rect x="3.5" y="10.8" width="6" height="1.5" fill="var(--teal)"/>
          </svg>
          <span>www.pacewithusfitness.com.au</span>
        </li>
      </ul>
    </section>

    <div class="divider"></div>

    <section class="brand">
      <span class="brand__dot"></span>
      <span class="brand__name">Pace with Us Fitness</span>
    </section>
  </main>
</body>
</html>
```